Corporate Design für Apotheke
Zielgruppe
Gesundheitswesen, Apotheke Zielgruppe kranke Menschen aber auch 'shopper'.
Aufgabenstellung
Das alte Logo ist leider viel zu filigran. Bei verschiedenen Druck kommt es oft nicht raus. Früher war das Logo eckig, es wurde vor Jahren mal als rund modernisiert.
Bin aber offen für alles.
Apotheke sollte grundsätzlich mit den Werten Seriosität, Vertrauen , und in unserem Fall auch Exklusivität, Premium- Segment verbunden werden. Im Anhang unser altes Logo. Ich bin zum ersten mal hier und freue mich auf kreative Vorschläge

```html
<!DOCTYPE html>
<html lang="de">
<head>
<meta charset="utf-8">
<title>Lindenhain-Apotheke – Corporate Design</title>
<link rel="stylesheet" href="https://fonts.googleapis.com/css2?family=Fira+Sans:wght@400;500&family=Caveat:wght@400&display=swap">
<style>
  :root {
    --green: #154734;
    --rose: #d4145a;
    --paper: #ffffff;
    --paper-back: #f3f3f2;
    --desk: #e6e6e4;
    --shadow: rgba(0,0,0,0.12);
  }
  * { margin: 0; padding: 0; box-sizing: border-box; }
  html, body { width: 1200px; height: 1134px; overflow: hidden; }
  body { position: relative; background: var(--paper); font-family: "Fira Sans", Arial, sans-serif; }

  .brand { position: absolute; left: 0; width: 100%; text-align: center; }
  .brand-mark { display: block; margin: 0 auto; border-radius: 50%; background: var(--green); }
  .brand-name { font-weight: 400; color: var(--green); line-height: 1; white-space: nowrap; letter-spacing: 0.02em; }
  .brand-tagline { font-family: "Caveat", cursive; color: var(--rose); line-height: 1; white-space: nowrap; }

  .intro { position: absolute; top: 0; left: 0; width: 1200px; height: 207px; background: var(--paper); }
  .intro .brand { top: 33px; }
  .intro .brand-mark { width: 76px; height: 76px; }
  .intro .brand-name { font-size: 24px; margin-top: 12px; }
  .intro .brand-tagline { font-size: 21px; margin-top: 3px; }

  .stationery { position: absolute; top: 207px; left: 0; width: 1200px; height: 718px; background: var(--desk); }
  .sheet { position: absolute; background: var(--paper); box-shadow: 0 2px 8px var(--shadow); overflow: hidden; }
  .sheet-back { left: 88px; top: 100px; width: 413px; height: 584px; background: var(--paper-back); }
  .letterhead { left: 257px; top: 51px; width: 414px; height: 584px; }
  .letterhead .brand { top: 21px; }
  .letterhead .brand-mark { width: 36px; height: 36px; }
  .letterhead .brand-name { font-size: 11px; margin-top: 5px; }
  .letterhead .brand-tagline { font-size: 9px; margin-top: 1px; }

  .band { position: absolute; left: 0; bottom: 0; width: 100%; display: block; }
  .band-text { position: absolute; left: 0; width: 100%; text-align: center; color: var(--paper); font-weight: 500; line-height: 1.55; white-space: nowrap; }
  .letterhead .band-text { bottom: 19px; font-size: 4.8px; }

  .business-card { width: 167px; height: 106px; left: 705px; }
  .card-front { top: 113px; }
  .card-back { top: 245px; }
  .business-card .brand { top: 9px; }
  .business-card .brand-mark { width: 30px; height: 30px; }
  .card-front .brand-name { font-size: 9.5px; margin-top: 4px; }
  .card-front .brand-tagline { font-size: 7.5px; }
  .card-front .band-text { bottom: 14px; font-size: 5.5px; }
  .card-contact { position: absolute; top: 50px; left: 0; width: 100%; text-align: center; font-size: 5.4px; font-weight: 500; color: var(--green); line-height: 1.45; white-space: nowrap; }
  .card-back .band-text { bottom: 10px; font-size: 5.4px; line-height: 1.45; }

  .envelope { left: 708px; top: 407px; width: 393px; height: 196px; }
  .envelope .brand { top: 15px; left: auto; right: 0; width: 202px; }
  .envelope .brand-mark { width: 30px; height: 30px; }
  .envelope .brand-name { font-size: 9.5px; margin-top: 4px; }
  .envelope .brand-tagline { font-size: 7.5px; }

  .outro { position: absolute; top: 925px; left: 0; width: 1200px; height: 209px; background: var(--green); }
  .outro .brand { top: 42px; }
  .outro .brand-mark { width: 68px; height: 68px; background: var(--paper); }
  .outro .brand-name { font-size: 22px; color: var(--paper); margin-top: 10px; }
  .outro .brand-tagline { font-size: 19px; color: var(--paper); margin-top: 2px; }
</style>
</head>
<body>

<header class="intro">
  <div class="brand">
    <span class="brand-mark"></span>
    <div class="brand-name">Lindenhain-Apotheke</div>
    <div class="brand-tagline">Ihr Wohlbefinden in Talbrunn</div>
  </div>
</header>

<main class="stationery">
  <div class="sheet sheet-back"></div>

  <section class="sheet letterhead">
    <div class="brand">
      <span class="brand-mark"></span>
      <div class="brand-name">Lindenhain-Apotheke</div>
      <div class="brand-tagline">Ihr Wohlbefinden in Talbrunn</div>
    </div>
    <svg class="band" width="414" height="64" viewBox="0 0 414 64" aria-hidden="true">
      <path d="M0 15 Q207 -8 414 15 L414 64 L0 64 Z" fill="var(--green)"/>
    </svg>
    <div class="band-text">
      Lindenhain-Apotheke | Geschäftsführerin Dr. Marta Seling e.K. | Mühlenweg 12 | 79999 Talbrunn<br>
      Telefon (0000) 12 34 56 | Fax (0000) 12 34 57 | info@lindenhain-apotheke.de | www.lindenhain-apotheke.de<br>
      Bank Talbrunn | IBAN DE 0000 000 000 000 0000 | BIC ABC000 000 | HRA 0000, Amtsgericht Talbrunn | Ust-IdNr: DE000000000
    </div>
  </section>

  <section class="sheet business-card card-front">
    <div class="brand">
      <span class="brand-mark"></span>
      <div class="brand-name">Lindenhain-Apotheke</div>
      <div class="brand-tagline">Ihr Wohlbefinden in Talbrunn</div>
    </div>
    <svg class="band" width="167" height="32" viewBox="0 0 167 32" aria-hidden="true">
      <path d="M0 6 Q83 -4 167 6 L167 32 L0 32 Z" fill="var(--green)"/>
    </svg>
    <div class="band-text">Mühlenweg 12, 79999 Talbrunn</div>
  </section>

  <section class="sheet business-card card-back">
    <div class="brand"><span class="brand-mark"></span></div>
    <div class="card-contact">
      Telefon (0000) 12 34 56 | Fax (0000) 12 34 57<br>
      info@lindenhain-apotheke.de | www.lindenhain-apotheke.de
    </div>
    <svg class="band" width="167" height="32" viewBox="0 0 167 32" aria-hidden="true">
      <path d="M0 0 Q83 -1 167 6 L167 32 L0 32 Z" fill="var(--green)"/>
    </svg>
    <div class="band-text">
      Öffnungszeiten:<br>
      Mo-Fr 8:00-12:30 Uhr, 14:30-18:00 Uhr | Sa 9:00-12:30 Uhr
    </div>
  </section>

  <section class="sheet envelope">
    <div class="brand">
      <span class="brand-mark"></span>
      <div class="brand-name">Lindenhain-Apotheke</div>
      <div class="brand-tagline">Ihr Wohlbefinden in Talbrunn</div>
    </div>
  </section>
</main>

<footer class="outro">
  <div class="brand">
    <span class="brand-mark"></span>
    <div class="brand-name">Lindenhain-Apotheke</div>
    <div class="brand-tagline">Ihr Wohlbefinden in Talbrunn</div>
  </div>
</footer>

</body>
</html>
```